A book about police officer shootings needs a dynamic cover design

I've almost completed a book on officer involved shootings...a very hot topic today. The title is "R.K.V. Beyond The Silence Broke." (emphasis on "Beyond The Silence") It details three separate shooting incidents, all within the same law enforcement family.I need a professional looking book cover that helps capture the drama. I attached a file of something I put together that is close, but I am concerned about "readability" and want a more professional look. I included a photo that I took off the internet of a gun being shot. That particular photo can stay or go, or be altered, but I like the perspective of the photo being fired from the person behind it. I wanted the cover to have the characteristics and color of a police uniform, utilizing blues, silvers, and maybe a little gold. I'm concerned about making sure the font and colors are also easy to read. I also will be working on a website design for "Beyond The Silence.Com" once the book hits the market. The back cover will incorporate the same colors, but only be a picture and excerpts from the book. I've included both for your review.

Target Market(s)

Law Enforcement, Christian, Media

Font styles to use
Sans Serif

Requirements
Must have
• A professional and readable appearance, that captures the drama of the topic. All the wording on the sample cover I attached, unless you come up with something better. A gun being fired from the perspective of the officer pulling the trigger. The size of the book will be the standard 6 x 9 in size. "Beyond The Silence" will eventually be my website domain and social media promotion hashtag.
Nice to have
• I would like the cover to incorporate the colors of a police uniform and badge, traditionally, navy blue, silver and some gold.
Should not have
• No police badge with a black band across. Not my topic.

```html
<!DOCTYPE html>
<html lang="en">
<head>
<meta charset="utf-8">
<title>R.K.V. Beyond The Silence Broke. – Cover Spread</title>
<link href="https://fonts.googleapis.com/css2?family=Archivo+Black&family=Arimo:wght@400;700&family=Oswald:wght@500;600&display=swap" rel="stylesheet">
<style>
  :root {
    --page: #ffffff;
    --ink-dark: #05080f;
    --navy: #0b1a33;
    --navy-glow: #1f4f86;
    --frame: #2f5f7e;
    --white: #ffffff;
    --silver-hi: #ffffff;
    --silver-lo: #9aa3ad;
    --muted: #9aa6b5;
    --tag: #f1e6b8;
    --flash: #ffb347;
    --flash-core: #fff3d6;
  }
  * { box-sizing: border-box; margin: 0; padding: 0; }
  html, body { width: 1100px; height: 1200px; overflow: hidden; background: var(--page); }
  .canvas { position: relative; width: 1100px; height: 1200px; }

  .spread {
    position: absolute; left: 56px; top: 42px; width: 982px; height: 644px;
    background: var(--ink-dark); overflow: hidden;
    font-family: "Arimo", Arial, sans-serif; color: var(--white);
  }

  /* Back cover */
  .back {
    position: absolute; left: 0; top: 0; width: 434px; height: 644px;
    background: radial-gradient(ellipse 70% 55% at 65% 42%, var(--navy-glow) 0%, var(--navy) 45%, var(--ink-dark) 85%);
  }
  .back-casing {
    position: absolute; left: 350px; top: 160px; width: 90px; height: 120px;
    background: radial-gradient(ellipse at 50% 50%, rgba(170,180,190,.35), rgba(0,0,0,0) 70%);
  }
  .author-photo {
    position: absolute; left: 37px; top: 37px; width: 200px; height: 231px;
    border: 4px solid var(--frame);
    background: linear-gradient(180deg, #8fb0d6 0%, #b8c4cf 40%, #4a4e56 70%, #2a2d33 100%);
  }
  .photo-captions {
    position: absolute; left: 37px; top: 271px; width: 200px;
    display: flex; justify-content: space-between; font-size: 9px; color: #c9d2dc;
  }
  .back-quote {
    position: absolute; left: 248px; top: 38px; width: 180px;
    font-family: "Oswald", sans-serif; font-weight: 500; font-size: 19px; line-height: 23px;
  }
  .excerpts { position: absolute; left: 18px; top: 292px; width: 408px; text-align: center; }
  .excerpt + .excerpt { margin-top: 14px; }
  .excerpt h3 { font-size: 10px; font-weight: 700; margin-bottom: 6px; }
  .excerpt p { font-size: 9.3px; font-weight: 700; line-height: 11.4px; }
  .publisher-note {
    position: absolute; left: 258px; top: 566px; width: 150px;
    text-align: center; font-size: 9px; line-height: 11px; color: #d5dbe2;
  }

  /* Spine */
  .spine {
    position: absolute; left: 434px; top: 0; width: 113px; height: 644px;
    background: linear-gradient(90deg, #030509, #0a0e16 50%, #030509);
  }
  .spine-title {
    position: absolute; left: 30px; top: 22px; writing-mode: vertical-rl;
    font-family: "Archivo Black", sans-serif; font-size: 24px; line-height: 1;
    background: linear-gradient(90deg, var(--silver-lo), var(--silver-hi) 50%, var(--silver-lo));
    -webkit-background-clip: text; background-clip: text; color: transparent;
  }
  .spine-title .big { font-size: 40px; }
  .spine-author {
    position: absolute; left: 74px; top: 450px; writing-mode: vertical-rl;
    font-weight: 700; font-size: 15px; color: var(--muted);
  }
  .spine-publisher {
    position: absolute; left: 0; top: 592px; width: 113px; text-align: center;
    font-weight: 700; font-size: 10px; line-height: 14px;
  }

  /* Front cover */
  .front { position: absolute; left: 547px; top: 0; width: 435px; height: 644px; }
  .front-art {
    position: absolute; inset: 0;
    background:
      radial-gradient(ellipse 55% 22% at 45% 43%, var(--flash-core) 0%, var(--flash) 35%, rgba(200,80,30,.4) 65%, rgba(0,0,0,0) 100%),
      radial-gradient(ellipse 40% 30% at 48% 72%, #2a3a55 0%, rgba(0,0,0,0) 100%),
      linear-gradient(180deg, #060a14 0%, #142746 50%, #0a1222 100%);
  }
  .front-quote {
    position: absolute; left: 0; top: 20px; width: 435px; text-align: center;
    font-family: "Oswald", sans-serif; font-weight: 500; font-size: 17px;
  }
  .front-title {
    position: absolute; left: 36px; top: 56px;
    font-family: "Archivo Black", sans-serif; line-height: 1;
    background: linear-gradient(180deg, var(--silver-hi) 20%, var(--silver-lo) 100%);
    -webkit-background-clip: text; background-clip: text; color: transparent;
  }
  .front-title .initials { font-size: 56px; letter-spacing: -1px; }
  .front-title .line { font-size: 31px; }
  .front-byline {
    position: absolute; right: 28px; top: 560px;
    font-family: "Arimo", sans-serif; font-weight: 700; font-size: 36px; letter-spacing: -.5px;
  }
  .front-byline small { font-size: 18px; }
  .front-tagline {
    position: absolute; left: 0; top: 606px; width: 435px; text-align: center;
    font-family: "Oswald", sans-serif; font-weight: 500; font-size: 15px; color: var(--tag);
  }
</style>
</head>
<body>
<div class="canvas">
  <section class="spread">

    <div class="back">
      <div class="back-casing" role="img" aria-label="Spent brass shell casing glowing in blue light"></div>
      <div class="author-photo" role="img" aria-label="Photograph of the three family officers standing together outdoors"></div>
      <div class="photo-captions"><span>Lt. Dale Harmon</span><span>Wade Harmon</span><span>Cole Harmon</span></div>
      <p class="back-quote">“You cannot rely on anyone but yourself to save your life...”</p>

      <div class="excerpts">
        <article class="excerpt">
          <h3>Dale's Story</h3>
          <p>“And then I heard it. The unmistakable sound of a shotgun being racked. And then another one. I was hit with near-blinding light from police flashlights, but was still able to make out the silhouettes of officers taking cover behind their patrol car doors... All weapons pointed directly at me...”</p>
        </article>
        <article class="excerpt">
          <h3>Wade's Story</h3>
          <p>“Wade stood over him, holding the shotgun in his left hand and his now empty handgun in his right. He stood there in stunned disbelief at how a routine call had escalated into a violent confrontation in a matter of seconds. The stench emanating from the house, mixed with the smell of gunpowder and blood, was almost overwhelming.”</p>
        </article>
        <article class="excerpt">
          <h3>Cole's Story</h3>
          <p>“Cole desperately wanted to stay with Sam, but the danger still presented by Kessler was paramount. As Cole rushed towards the suspended vehicle, the door suddenly opened. Kessler climbed out and dropped to the ground. He stood and faced Cole like a raging bull. If the bull charged, Cole was prepared to shoot again...”</p>
        </article>
      </div>

      <p class="publisher-note">Publisher Logo and other<br>Publisher information go here</p>
    </div>

    <div class="spine">
      <div class="spine-title"><span class="big">R.K.V.</span> BEYOND THE SILENCE BROKE.</div>
      <div class="spine-author">Lt. Dale Harmon</div>
      <div class="spine-publisher">Publisher<br>Logo</div>
    </div>

    <div class="front">
      <div class="front-art" role="img" aria-label="Handgun seen from behind the shooter's grip, muzzle flash bursting in orange light"></div>
      <p class="front-quote">“It WILL happen, and it will come out of nowhere...”</p>
      <h1 class="front-title">
        <span class="initials">R.K.V.</span> <span class="line">BEYOND THE</span><br>
        <span class="line">SILENCE BROKE.</span>
      </h1>
      <p class="front-byline"><small>by </small>Lt. Dale Harmon</p>
      <p class="front-tagline">One Law Enforcement Family... Three Life Changing Stories</p>
    </div>

  </section>
</div>
</body>
</html>
```